Signage setout with photos for side of Mowing Trailer

We need signage for our mowing trailer to attract new business.
Specifically a Rear sign 1470x880mm and Side signs 2400x880mm
Sign needs to be modern and professional.
Some example uploads as to what we have thought about so far.
Logo doesn't need to be the green colour.
Logo words and Logo of Mower do not need to be together.
Link to get a mower image>
https://bluefernmachinery.com/torvo
Updates

Need extra days to review

Target Market(s)

Other Customers driving past the trailer.

Industry/Entity Type

Lawnmowing / Landscaping

Requirements
Must have
• Phone Number, Company Name & Logo, Web address, Facebook and Insta Logos, Comment - "Acreage & Commercial Specialists" Catchcry - "100% Electric Mowing Company - est 2017" Services "Mowing, Hedging, Pressure Cleaning, Weed Control, Fencing, Turfing, Mulching and Rubbish Removal"
Nice to have
• Full colour background images.

```html
<!DOCTYPE html>
<html lang="en">
<head>
<meta charset="utf-8">
<title>Fresh Field Mowing – Trailer Sign</title>
<link rel="stylesheet" href="https://fonts.googleapis.com/css2?family=Montserrat:wght@600;700;800&display=swap">
<style>
  :root {
    --backdrop: #c4c4c4;
    --grass-dark: #2f6a24;
    --grass-mid: #3f8a2e;
    --grass-light: #5aa63c;
    --brand-green: #1f7a3c;
    --accent-orange: #ec6a22;
    --white: #ffffff;
    --mower-green: #5fd12a;
  }
  html, body {
    margin: 0;
    width: 1200px;
    height: 1200px;
    overflow: hidden;
    background: var(--backdrop);
    font-family: 'Montserrat', sans-serif;
  }
  .sign {
    position: absolute;
    left: 97px;
    top: 416px;
    width: 1006px;
    height: 368px;
    overflow: hidden;
    background: linear-gradient(180deg, var(--grass-light) 0%, var(--grass-mid) 35%, var(--grass-dark) 100%);
    color: var(--white);
  }
  .sign-shape { position: absolute; inset: 0; }
  .brand-name {
    position: absolute; left: 33px; top: 82px;
    font-weight: 700; font-size: 15px; line-height: 18px;
    text-align: center; letter-spacing: 0.2px;
  }
  .brand-name .big { font-size: 19px; letter-spacing: 0.6px; }
  .brand-dot {
    position: absolute; left: 60px; top: 30px;
    width: 40px; height: 40px; border-radius: 50%;
    background: var(--white);
  }
  .headline {
    position: absolute; left: 161px; top: 22px;
    font-weight: 800; font-size: 39px; letter-spacing: -0.3px; margin: 0;
    white-space: nowrap;
  }
  .headline .amp { font-weight: 600; }
  .specialists {
    position: absolute; left: 159px; top: 72px;
    padding: 0 8px; height: 36px; line-height: 38px;
    background: #f1f1f1; color: var(--brand-green);
    font-weight: 800; font-size: 33px;
  }
  .electric-percent {
    position: absolute; left: 152px; top: 122px;
    font-weight: 800; font-size: 56px; letter-spacing: -3px;
    color: var(--brand-green);
    -webkit-text-stroke: 2px var(--white);
  }
  .electric-line {
    position: absolute; left: 290px; top: 127px;
    font-weight: 700; font-size: 22px; white-space: nowrap;
  }
  .company-tag {
    position: absolute; left: 290px; top: 154px;
    background: var(--accent-orange); padding: 0 4px;
    height: 24px; line-height: 25px;
    font-weight: 700; font-size: 21px;
  }
  .est {
    position: absolute; left: 414px; top: 155px;
    font-weight: 800; font-size: 17px; color: var(--accent-orange);
    -webkit-text-stroke: 0.6px var(--white);
  }
  .service {
    position: absolute; font-weight: 700; font-size: 16px; line-height: 22px;
    text-transform: uppercase;
  }
  .service svg { position: absolute; left: -35px; top: 2px; }
  .phone-icon { position: absolute; left: 22px; top: 314px; }
  .phone-number {
    position: absolute; left: 77px; top: 306px;
    font-weight: 700; font-size: 40px; letter-spacing: 0.5px;
  }
  .follow {
    position: absolute; left: 353px; top: 314px;
    font-weight: 700; font-size: 14px;
  }
  .social-dot {
    position: absolute; top: 306px; width: 22px; height: 22px;
    border-radius: 50%; background: var(--white);
  }
  .globe-icon { position: absolute; left: 325px; top: 333px; }
  .web {
    position: absolute; left: 355px; top: 334px;
    font-weight: 700; font-size: 14px;
  }
  .mower-photo {
    position: absolute; left: 723px; top: 36px;
    width: 264px; height: 296px; border-radius: 18px;
    background: radial-gradient(ellipse at 50% 70%, var(--mower-green) 0%, #4aa52a 45%, #eef3ea 80%);
  }
</style>
</head>
<body>
<main class="sign">
  <svg class="sign-shape" width="1006" height="368" viewBox="0 0 1006 368" aria-hidden="true">
    <path d="M768 0 Q524 184 768 368 L1006 368 L1006 0 Z" fill="var(--accent-orange)"/>
    <path d="M792 0 Q552 184 792 368 L1006 368 L1006 0 Z" fill="var(--white)"/>
  </svg>

  <div class="brand-dot"></div>
  <div class="brand-name">FRESH FIELD<br><span class="big">MOWING</span></div>

  <h1 class="headline">ACREAGE <span class="amp">&amp;</span> COMMERCIAL</h1>
  <div class="specialists">SPECIALISTS</div>

  <div class="electric-percent">100%</div>
  <div class="electric-line">ELECTRIC MOWING</div>
  <div class="company-tag">COMPANY</div>
  <div class="est">EST - 2017</div>

  <div class="service" style="left:74px;top:197px">Mowing<svg width="22" height="14" viewBox="0 0 22 14"><path d="M1 3 Q12 -2 21 10 Q10 14 1 3Z" fill="var(--accent-orange)"/></svg></div>
  <div class="service" style="left:229px;top:197px">Turfing<svg width="22" height="14" viewBox="0 0 22 14"><path d="M1 3 Q12 -2 21 10 Q10 14 1 3Z" fill="var(--accent-orange)"/></svg></div>
  <div class="service" style="left:379px;top:193px">Mulching<svg width="22" height="14" viewBox="0 0 22 14"><path d="M1 3 Q12 -2 21 10 Q10 14 1 3Z" fill="var(--accent-orange)"/></svg></div>
  <div class="service" style="left:550px;top:193px">Pressure<br>Cleaning<svg width="22" height="14" viewBox="0 0 22 14"><path d="M1 3 Q12 -2 21 10 Q10 14 1 3Z" fill="var(--accent-orange)"/></svg></div>
  <div class="service" style="left:71px;top:240px">Hedging<svg width="22" height="14" viewBox="0 0 22 14"><path d="M1 3 Q12 -2 21 10 Q10 14 1 3Z" fill="var(--accent-orange)"/></svg></div>
  <div class="service" style="left:226px;top:240px">Fencing<svg width="22" height="14" viewBox="0 0 22 14"><path d="M1 3 Q12 -2 21 10 Q10 14 1 3Z" fill="var(--accent-orange)"/></svg></div>
  <div class="service" style="left:376px;top:240px">Weed<br>Control<svg width="22" height="14" viewBox="0 0 22 14"><path d="M1 3 Q12 -2 21 10 Q10 14 1 3Z" fill="var(--accent-orange)"/></svg></div>
  <div class="service" style="left:553px;top:240px">Rubbish<br>Removal<svg width="22" height="14" viewBox="0 0 22 14"><path d="M1 3 Q12 -2 21 10 Q10 14 1 3Z" fill="var(--accent-orange)"/></svg></div>

  <svg class="phone-icon" width="40" height="40" viewBox="0 0 40 40" aria-hidden="true">
    <circle cx="20" cy="20" r="20" fill="var(--white)"/>
    <path d="M13 10 L17 10 L19 16 L16 18 Q18 23 22 25 L24 22 L30 24 L30 28 Q29 31 26 31 Q12 29 10 14 Q10 11 13 10Z" fill="var(--grass-dark)"/>
  </svg>
  <div class="phone-number">3555 0142</div>

  <div class="follow">FOLLOW US</div>
  <div class="social-dot" style="left:456px"></div>
  <div class="social-dot" style="left:494px"></div>

  <svg class="globe-icon" width="20" height="20" viewBox="0 0 20 20" aria-hidden="true">
    <circle cx="10" cy="10" r="8.5" fill="none" stroke="var(--white)" stroke-width="2"/>
    <ellipse cx="10" cy="10" rx="3.5" ry="8.5" fill="none" stroke="var(--white)" stroke-width="1.5"/>
    <line x1="2" y1="10" x2="18" y2="10" stroke="var(--white)" stroke-width="1.5"/>
  </svg>
  <div class="web">WWW.FRESHFIELDMOWING.COM.AU</div>

  <div class="mower-photo" role="img" aria-label="Photo of a bright green electric zero-turn ride-on mower with a canopy roof"></div>
</main>
</body>
</html>
```